Email Signiture and letterhead design

we are looking for a modern business design to incorporate our logo and iso certification plus social icons for Twitter, LinkedIn, and youtube
they must include our UK vat and also company registration as text but I can fill these out. Email signature to have a link/icon to our webshop www.dremlox.co.uk

Target Market(s)

All

Font styles to use
Serif
Sans Serif

Requirements
Must have
• Address, tel, email , web details incorperated
Nice to have
• a professional looking letter head and email signiture, Email signature to have a link/icon to our webshop www.dremlox.co.uk

```html
<!DOCTYPE html>
<html lang="en">
<head>
<meta charset="utf-8">
<title>Dremlox Hubs &amp; Bearings Ltd — Letterhead and Email Signature</title>
<link href="https://fonts.googleapis.com/css2?family=Lato:wght@400;700&family=Great+Vibes&display=swap" rel="stylesheet">
<style>
  :root {
    --backdrop: #dcdbdd;
    --paper: #f6f5f6;
    --ink: #2b2b2d;
    --ink-soft: #3a3a3c;
    --brand-red: #e31b23;
    --band-dark: #3b3b3d;
    --badge-fill: #e9e7ea;
    --badge-edge: #c9c6cb;
    --badge-accent: #e0177a;
    --social: #8a8a8e;
  }
  * { margin: 0; padding: 0; box-sizing: border-box; }
  html, body { width: 1200px; height: 985px; overflow: hidden; }
  body {
    position: relative;
    background: var(--backdrop);
    font-family: "Lato", Arial, sans-serif;
    color: var(--ink);
  }

  /* ---------- Letterhead ---------- */
  .letterhead {
    position: absolute;
    left: 52px; top: 75px;
    width: 597px; height: 848px;
    background: radial-gradient(ellipse at 55% 35%, #ffffff 0%, var(--paper) 70%);
    overflow: hidden;
  }
  .brand {
    display: flex; align-items: center; gap: 7px;
    font-weight: 700; color: var(--ink-soft);
    white-space: nowrap;
  }
  .brand-dot { border-radius: 50%; background: var(--brand-red); flex: none; }
  .letterhead .brand { position: absolute; left: 42px; top: 94px; font-size: 15px; }
  .letterhead .brand-dot { width: 14px; height: 14px; }

  .contact-block {
    position: absolute; left: 443px; top: 35px;
    border-left: 1px solid var(--brand-red);
    padding-left: 6px;
    font-size: 10px; line-height: 15.5px;
  }
  .contact-block .address { margin-bottom: 5px; }
  .contact-line { display: flex; align-items: center; gap: 6px; }
  .icon { fill: var(--brand-red); flex: none; }

  .letter-body {
    position: absolute; left: 46px; top: 194px; width: 505px;
    font-size: 11.4px; line-height: 13px; color: var(--ink-soft);
  }
  .letter-date { margin-bottom: 15px; }
  .recipient { margin-bottom: 14px; }
  .salutation { font-size: 14px; font-weight: 700; margin: 4px 0 14px; }
  .letter-body p.para { text-align: justify; margin-bottom: 13px; }
  .closing { margin-top: 26px; }
  .signature {
    font-family: "Great Vibes", cursive;
    font-size: 30px; color: var(--ink); margin-top: 16px; line-height: 1;
  }
  .letterhead .footer-wave { position: absolute; left: 0; bottom: 0; width: 597px; height: 70px; }

  /* ---------- Email signature ---------- */
  .email-signature {
    position: absolute; left: 666px; top: 372px;
    width: 488px; height: 174px;
    background: linear-gradient(180deg, #ffffff 0%, var(--paper) 100%);
    overflow: hidden;
  }
  .email-signature .brand { position: absolute; left: 23px; top: 44px; font-size: 10px; gap: 5px; }
  .email-signature .brand-dot { width: 10px; height: 10px; }
  .divider { position: absolute; width: 2px; background: var(--brand-red); top: 28px; height: 48px; }
  .divider.first { left: 184px; }
  .divider.second { left: 336px; }
  .iso-badge {
    position: absolute; left: 203px; top: 28px; width: 113px; height: 42px;
    border-radius: 7px; background: var(--badge-fill);
    border: 1.5px solid var(--badge-edge);
    overflow: hidden;
  }
  .iso-badge::after {
    content: ""; position: absolute; right: 0; top: 0; width: 12px; height: 100%;
    background: var(--badge-accent);
  }
  .sig-contacts {
    position: absolute; left: 349px; top: 25px;
    font-size: 12.5px; line-height: 18.5px;
  }
  .sig-contacts .contact-line { gap: 7px; }
  .sig-address { position: absolute; left: 23px; top: 103px; font-size: 12.5px; }
  .social-links { position: absolute; left: 383px; top: 96px; display: flex; gap: 8px; }
  .social-links span { width: 20px; height: 20px; border-radius: 50%; background: var(--social); }
  .email-signature .footer-wave { position: absolute; left: 0; bottom: 0; width: 488px; height: 60px; }
</style>
</head>
<body>

  <section class="letterhead">
    <div class="brand"><span class="brand-dot"></span>Dremlox Hubs &amp; Bearings Ltd</div>

    <div class="contact-block">
      <div class="address">42-07 Harlow Ave 16<br>Ridgeview, NY 11420</div>
      <div class="contact-line">
        <svg class="icon" width="9" height="9" viewBox="0 0 24 24"><path d="M6.6 10.8a15 15 0 0 0 6.6 6.6l2.2-2.2a1 1 0 0 1 1-.25 11.4 11.4 0 0 0 3.6.57 1 1 0 0 1 1 1V20a1 1 0 0 1-1 1A17 17 0 0 1 3 4a1 1 0 0 1 1-1h3.5a1 1 0 0 1 1 1c0 1.25.2 2.45.57 3.57a1 1 0 0 1-.25 1z"/></svg>
        555-0142-7781
      </div>
      <div class="contact-line">
        <svg class="icon" width="9" height="9" viewBox="0 0 24 24"><path d="M2 5h20v14H2z M2 5l10 8 10-8" /></svg>
        info@dremlox.co.uk
      </div>
      <div class="contact-line">
        <svg class="icon" width="9" height="9" viewBox="0 0 24 24"><circle cx="12" cy="12" r="10"/></svg>
        www.dremlox.co.uk
      </div>
    </div>

    <div class="letter-body">
      <p class="letter-date">Feb-03-2022</p>
      <p class="recipient">Mr, Peter Lane<br>President</p>
      <p class="recipient">Norvane Corporation<br>123 Street Name, Suite# 10<br>City, State, 120023</p>
      <p class="salutation">Dear Mr, Peter</p>
      <p class="para">Lorem ipsum dolor sit amet, consectetur adipisicing elit, sed do eiusmod tempor incididunt ut labore et dolore magna aliqua. Ut enim ad minim veniam, quis nostrud exercitation ullamco laboris nisi ut aliquip ex ea commodo consequat. Duis aute irure dolor in reprehenderit in voluptate velit esse cillum dolore eu fugiat nulla pariatur.</p>
      <p class="para">Lorem ipsum dolor sit amet, consectetur adipisicing elit, sed do eiusmod tempor incididunt ut labore et dolore magna aliqua. Ut enim ad minim veniam, quis nostrud exercitation ullamco laboris nisi ut aliquip ex ea commodo consequat. Duis aute irure dolor in reprehenderit in voluptate velit esse cillum dolore eu fugiat nulla pariatur.</p>
      <p class="para">Lorem ipsum dolor sit amet, consectetur adipisicing elit, sed do eiusmod tempor incididunt ut labore et dolore magna aliqua. Ut enim ad minim veniam, quis nostrud exercitation ullamco laboris nisi ut aliquip ex ea commodo consequat.</p>
      <p class="para">Excepteur sint occaecat cupidatat non proident, sunt in culpa qui officia deserunt mollit anim id est laborum. re et dolore magnam aliquam quaerat voluptatem.</p>
      <p class="closing">Regards</p>
      <p class="signature">Daniel Hart</p>
    </div>

    <svg class="footer-wave" viewBox="0 0 597 70" preserveAspectRatio="none">
      <path d="M0 14 Q300 44 597 14 L597 70 L0 70Z" fill="var(--band-dark)"/>
      <path d="M120 22 Q400 30 597 0 L597 11 Q400 36 120 22Z" fill="var(--brand-red)"/>
    </svg>
  </section>

  <section class="email-signature">
    <div class="brand"><span class="brand-dot"></span>Dremlox Hubs &amp; Bearings Ltd</div>
    <span class="divider first"></span>
    <div class="iso-badge" role="img" aria-label="Quality management certification badge"></div>
    <span class="divider second"></span>

    <div class="sig-contacts">
      <div class="contact-line">
        <svg class="icon" width="11" height="11" viewBox="0 0 24 24"><path d="M6.6 10.8a15 15 0 0 0 6.6 6.6l2.2-2.2a1 1 0 0 1 1-.25 11.4 11.4 0 0 0 3.6.57 1 1 0 0 1 1 1V20a1 1 0 0 1-1 1A17 17 0 0 1 3 4a1 1 0 0 1 1-1h3.5a1 1 0 0 1 1 1c0 1.25.2 2.45.57 3.57a1 1 0 0 1-.25 1z"/></svg>
        555-0142-7781
      </div>
      <div class="contact-line">
        <svg class="icon" width="11" height="11" viewBox="0 0 24 24"><path d="M2 5h20v14H2z M2 5l10 8 10-8"/></svg>
        info@dremlox.co.uk
      </div>
      <div class="contact-line">
        <svg class="icon" width="11" height="11" viewBox="0 0 24 24"><circle cx="12" cy="12" r="10"/></svg>
        www.dremlox.co.uk
      </div>
    </div>

    <p class="sig-address">42-07 Harlow Ave 16 Ridgeview, NY 11420</p>

    <div class="social-links" aria-label="Social profiles">
      <span></span><span></span><span></span>
    </div>

    <svg class="footer-wave" viewBox="0 0 488 60" preserveAspectRatio="none">
      <path d="M0 19 Q250 38 488 20 L488 60 L0 60Z" fill="var(--band-dark)"/>
      <path d="M90 28 Q320 34 488 8 L488 17 Q320 40 90 28Z" fill="var(--brand-red)"/>
    </svg>
  </section>

</body>
</html>
```